Create a MAIN PAGE that is so enticing they won't say no. -Nex Vol website

High traffic site but we are not closing the deal as much as we should. Our retention rate is 90%. We believe that our site is not properly conveying to our clients the wonderous, exotic and unique experiences we provide them. Our site must give the same impression we give in person. We are seeking a designer to revise our main page & booking pages as these are our calling card pages.
Our industry is selling fantasy and escapism. We want our main page to convey two high class, discreet, sexy dominatrix's.
We want our booking page to be user friendly.
www.velvetquarterhouse.net

Target Market(s)

Adult Men ages 45-65

Industry/Entity Type

Sex

Coding

Coded - Design and coding required

Number of Pages Required

2 page

Font styles to use
Serif

Colors
EB3D1F
EC4F4E
F09395
F8D3D4
FCEDEE

Requirements
Must have
• Black & Red color theme, animation, clean, classy, sexy
Nice to have
• Smoke effect on the main page
Should not have
• Should not look basic

```html
<!DOCTYPE html>
<html lang="en">
<head>
<meta charset="utf-8">
<title>Booking – Velvet Quarter House</title>
<link href="https://fonts.googleapis.com/css2?family=Anton&family=Inter:ital,wght@0,400;0,500;0,700;1,400&family=Mrs+Saint+Delafield&display=swap" rel="stylesheet">
<style>
:root{
  --ink:#000;
  --paper:#fff;
  --red:#e51a1a;
  --line:#cfcfcf;
  --hero-a:#14301f;
  --hero-b:#2a2a2a;
}
*{box-sizing:border-box;margin:0;padding:0}
html,body{width:1200px;height:2163px;overflow:hidden;background:var(--ink)}
body{position:relative;font-family:'Inter',sans-serif;color:var(--paper)}
.abs{position:absolute}
.hero{left:5px;top:0;width:1195px;height:538px;background:radial-gradient(ellipse at 50% 40%,#3a3030 0%,var(--hero-a) 55%,#0c1a12 100%)}
.hero-shade{left:0;top:0;width:1200px;height:538px;background:rgba(0,0,0,.35)}
.brand{left:80px;top:46px;font-size:19px;font-weight:500;letter-spacing:.2px}
.menu{left:1063px;top:46px}
.hero-title{left:0;width:1200px;top:260px;text-align:center;font-family:'Mrs Saint Delafield',cursive;font-size:96px;color:var(--red);line-height:1}
.hero-sub{left:0;width:1200px;top:418px;text-align:center;font-size:16px;line-height:24px}
.acc-head{left:80px;width:361px;font-family:'Anton',sans-serif;font-size:27px;letter-spacing:.3px;line-height:1}
.acc-rule{left:80px;width:361px;height:1px;background:var(--line)}
.chev{left:408px}
.acc-body{left:80px;top:736px;width:361px;font-size:13px;line-height:19.3px}
.form-title{left:582px;top:641px;width:450px;font-size:16px;line-height:20px}
.form-intro{left:582px;top:692px;width:450px;font-size:13px;line-height:19px}
.label{font-size:13px}
.field{border:1.5px solid var(--line);background:var(--ink)}
.placeholder{font-size:13px;font-style:italic;color:#9a9a9a;padding:17px 0 0 17px}
.check{display:flex;align-items:flex-start;gap:11px;font-size:13.5px;line-height:16px}
.box{width:12px;height:12px;border:1.5px solid var(--paper);flex:none;margin-top:2px}
.agree-title{left:584px;top:1589px;font-size:16px;color:var(--red)}
.note{left:589px;top:1802px;width:440px;font-size:13px;line-height:16px}
.submit{left:588px;top:1886px;width:109px;height:41px;background:var(--red);color:var(--paper);font-weight:700;font-size:16px;display:flex;align-items:center;justify-content:center;border:none}
.foot-rule{left:78px;top:2036px;width:1020px;height:1px;background:#3a3a3a}
.social{top:2068px;font-size:15px;font-weight:500}
.copyright{left:0;width:1200px;top:2109px;text-align:center;font-size:9px;font-weight:500}
</style>
</head>
<body>
<header>
  <div class="abs hero" role="img" aria-label="Photo of the two hostesses seated in a dim green room"></div>
  <div class="abs hero-shade"></div>
  <div class="abs brand">VELVET QUARTER HOUSE</div>
  <svg class="abs menu" width="38" height="22" viewBox="0 0 38 22"><g stroke="#fff" stroke-width="3"><line x1="0" y1="2" x2="38" y2="2"/><line x1="0" y1="11" x2="38" y2="11"/><line x1="0" y1="20" x2="38" y2="20"/></g></svg>
  <h1 class="abs hero-title">Booking Goddess &amp; Master</h1>
  <p class="abs hero-sub">The time you spend with us will be a Double Domme session,<br>we enjoy kink strictly as a duo.</p>
</header>

<section class="policies">
  <h2 class="abs acc-head" style="top:662px">SCHEDULE</h2>
  <svg class="abs chev" style="top:674px" width="20" height="12" viewBox="0 0 20 12"><polyline points="1,11 10,2 19,11" fill="none" stroke="#fff" stroke-width="1.8"/></svg>
  <div class="abs acc-rule" style="top:713px"></div>
  <p class="abs acc-body">We accept bookings Monday - Saturday. We can and do make exceptions if you tell us why you want to book us on a Sunday and send us a pretty substantial tribute. Then and only then will we consider it.</p>

  <h2 class="abs acc-head" style="top:849px">TRAVEL</h2>
  <svg class="abs chev" style="top:869px" width="20" height="12" viewBox="0 0 20 12"><polyline points="1,1 10,10 19,1" fill="none" stroke="#fff" stroke-width="1.8"/></svg>
  <div class="abs acc-rule" style="top:899px"></div>

  <h2 class="abs acc-head" style="top:917px">DEPOSITS</h2>
  <svg class="abs chev" style="top:933px" width="20" height="12" viewBox="0 0 20 12"><polyline points="1,1 10,10 19,1" fill="none" stroke="#fff" stroke-width="1.8"/></svg>
  <div class="abs acc-rule" style="top:967px"></div>

  <h2 class="abs acc-head" style="top:986px">CANCELLATIONS</h2>
  <svg class="abs chev" style="top:1012px" width="20" height="12" viewBox="0 0 20 12"><polyline points="1,1 10,10 19,1" fill="none" stroke="#fff" stroke-width="1.8"/></svg>
  <div class="abs acc-rule" style="top:1036px"></div>

  <h2 class="abs acc-head" style="top:1054px">MEET &amp; GREET</h2>
  <svg class="abs chev" style="top:1076px" width="20" height="12" viewBox="0 0 20 12"><polyline points="1,1 10,10 19,1" fill="none" stroke="#fff" stroke-width="1.8"/></svg>
  <div class="abs acc-rule" style="top:1104px"></div>

  <h2 class="abs acc-head" style="top:1123px">CONTACT US</h2>
  <svg class="abs chev" style="top:1149px" width="20" height="12" viewBox="0 0 20 12"><polyline points="1,1 10,10 19,1" fill="none" stroke="#fff" stroke-width="1.8"/></svg>
  <div class="abs acc-rule" style="top:1173px"></div>

  <h2 class="abs acc-head" style="top:1191px">OUR WISHLIST</h2>
  <svg class="abs chev" style="top:1213px" width="20" height="12" viewBox="0 0 20 12"><polyline points="1,1 10,10 19,1" fill="none" stroke="#fff" stroke-width="1.8"/></svg>
  <div class="abs acc-rule" style="top:1241px"></div>
</section>

<section class="booking-form">
  <h2 class="abs form-title" style="font-weight:400">TO BOOK TIME WITH SABLE &amp; ROWAN PLEASE COMPLETE THIS FORM &amp; SUBMIT IT.</h2>
  <p class="abs form-intro">Please read the questions and answer them to book your session with Master Sable &amp; Goddess Rowan.</p>

  <div class="abs label" style="left:584px;top:764px">Name*</div>
  <div class="abs label" style="left:826px;top:764px">Age -Must be 18 &amp; Over*</div>
  <div class="abs field" style="left:582px;top:786px;width:203px;height:50px"></div>
  <div class="abs field" style="left:820px;top:786px;width:203px;height:50px"></div>

  <div class="abs label" style="left:584px;top:861px">Phone Number*</div>
  <div class="abs label" style="left:826px;top:861px">Preferred date</div>
  <div class="abs field" style="left:582px;top:883px;width:203px;height:50px"></div>
  <div class="abs field" style="left:820px;top:883px;width:203px;height:50px"></div>

  <div class="abs label" style="left:584px;top:954px">What are you kinks/fetishes?*</div>
  <div class="abs field" style="left:582px;top:989px;width:441px;height:131px"></div>

  <div class="abs label" style="left:584px;top:1138px">Please list any medical conditions.*</div>
  <div class="abs field" style="left:582px;top:1172px;width:441px;height:46px"></div>

  <div class="abs label" style="left:582px;top:1251px">Preferred City/Location*</div>
  <div class="abs label" style="left:820px;top:1251px">Preferred Duration*</div>
  <div class="abs field" style="left:582px;top:1274px;width:203px;height:50px"><div class="placeholder">Add answer here</div></div>
  <div class="abs field" style="left:820px;top:1274px;width:203px;height:50px"></div>

  <div class="abs label" style="left:582px;top:1357px">How did you find out about us?</div>
  <div class="abs check" style="left:581px;top:1390px"><span class="box"></span>Seekly Search</div>
  <div class="abs check" style="left:581px;top:1417px"><span class="box"></span>ClipVault</div>
  <div class="abs check" style="left:581px;top:1447px"><span class="box"></span>Some awesome indvidual referred you?</div>
  <div class="abs check" style="left:581px;top:1473px"><span class="box"></span>A Pro Domme Directory site</div>
  <div class="abs check" style="left:581px;top:1502px"><span class="box"></span>Snapwall</div>
  <div class="abs check" style="left:581px;top:1529px"><span class="box"></span>FanPortal</div>

  <h3 class="abs agree-title" style="font-weight:400">AGREEMENTS</h3>
  <div class="abs check" style="left:584px;top:1632px;font-size:13px"><span class="box"></span>You are over the age of 18</div>
  <div class="abs check" style="left:584px;top:1661px;width:360px;font-size:13px"><span class="box"></span>You have read our Specialities and Interest list and will NOT ask for any services listed under the Limits/No Thank You section?</div>
  <div class="abs check" style="left:584px;top:1719px;width:320px;font-size:13px"><span class="box"></span>You have read and understand our deposit and cancellation policies?</div>

  <p class="abs note">Tribute must be presented in an unsealed envelope at the beginning of our time together.</p>
  <button class="abs submit">SUBMIT</button>
</section>

<footer>
  <div class="abs foot-rule"></div>
  <div class="abs social" style="left:520px">Chirper</div>
  <div class="abs social" style="left:590px">FanPortal</div>
  <p class="abs copyright">© 2022 VELVET QUARTER HOUSE. ALL RIGHTS RESERVED.</p>
</footer>
</body>
</html>
```